Refresh of Business Card Design

Want to refresh the business card design with the new logo while adhering to style guide as attached. Would like to match feel of website www.durmackvinex.com

```html
<!DOCTYPE html>
<html lang="en">
<head>
<meta charset="utf-8">
<title>Durmack Vinex – Business Card</title>
<link rel="stylesheet" href="https://fonts.googleapis.com/css2?family=Roboto+Condensed:wght@400&display=swap">
<style>
  :root {
    --stage: #e6e6ea;
    --brand-red: #e8204a;
    --ink-black: #0b0b0b;
    --paper-white: #ffffff;
    --card-w: 842px;
    --card-h: 492px;
  }
  * { box-sizing: border-box; margin: 0; padding: 0; }
  html, body { width: 1200px; height: 1200px; overflow: hidden; }
  body {
    background: var(--stage);
    font-family: "Roboto Condensed", "Arial Narrow", sans-serif;
    color: var(--paper-white);
    position: relative;
  }
  .card {
    position: absolute;
    left: 179px;
    width: var(--card-w);
    height: var(--card-h);
    background: var(--brand-red);
    overflow: hidden;
    box-shadow: 0 1px 3px rgba(0,0,0,0.12);
  }
  .card--front { top: 83px; }
  .card--back { top: 624px; }

  .brand-disc {
    position: absolute;
    border-radius: 50%;
    background: var(--ink-black);
  }
  .card--front .brand-disc {
    width: 412px; height: 412px;
    left: -23px; top: 42px;
  }
  .card--back .brand-disc {
    width: 304px; height: 304px;
    left: 269px; top: 93px;
  }
  .brand-name {
    position: absolute;
    font-weight: 400;
    letter-spacing: 0.04em;
    color: var(--paper-white);
    white-space: nowrap;
    transform: translate(-50%, -50%);
  }
  .card--front .brand-name { left: 183px; top: 248px; font-size: 26px; }
  .card--back .brand-name { left: 421px; top: 245px; font-size: 40px; }

  .person {
    position: absolute;
    right: 47px;
    top: 102px;
    text-align: right;
  }
  .person__name { font-size: 36px; line-height: 1.1; font-weight: 400; }
  .person__role { font-size: 19px; line-height: 1.2; }

  .contact {
    position: absolute;
    right: 44px;
    top: 287px;
    list-style: none;
    text-align: right;
  }
  .contact__item {
    display: flex;
    justify-content: flex-end;
    align-items: center;
    font-size: 20px;
    line-height: 32.5px;
    height: 32.5px;
  }
  .contact__icon {
    width: 14px; height: 14px;
    margin-left: 12px;
    flex: none;
    fill: var(--paper-white);
  }
  .contact__item--plain { padding-right: 26px; }
</style>
</head>
<body>

<section class="card card--front" aria-label="Card front">
  <div class="brand-disc"></div>
  <span class="brand-name">DURMACK VINEX</span>

  <div class="person">
    <h1 class="person__name">REID HALLOW</h1>
    <p class="person__role">Sales</p>
  </div>

  <ul class="contact">
    <li class="contact__item">555.201.3384
      <svg class="contact__icon" viewBox="0 0 24 24" aria-hidden="true"><path d="M6.6 10.8a15.1 15.1 0 0 0 6.6 6.6l2.2-2.2a1 1 0 0 1 1-.25 11.4 11.4 0 0 0 3.6.57 1 1 0 0 1 1 1V20a1 1 0 0 1-1 1A17 17 0 0 1 3 4a1 1 0 0 1 1-1h3.5a1 1 0 0 1 1 1c0 1.25.2 2.45.57 3.57a1 1 0 0 1-.25 1z"/></svg>
    </li>
    <li class="contact__item">rhallow@durmackvinex.com
      <svg class="contact__icon" viewBox="0 0 24 24" aria-hidden="true"><path d="M3 5h18a1 1 0 0 1 1 1v12a1 1 0 0 1-1 1H3a1 1 0 0 1-1-1V6a1 1 0 0 1 1-1zm9 7.5L20 7H4z"/></svg>
    </li>
    <li class="contact__item">www.durmackvinex.com
      <svg class="contact__icon" viewBox="0 0 24 24" aria-hidden="true"><path d="M12 2a10 10 0 1 0 0 20 10 10 0 0 0 0-20zm6.9 6h-3a15.6 15.6 0 0 0-1.4-3.6A8 8 0 0 1 18.9 8zM12 4c.8 1.2 1.5 2.5 1.9 4h-3.8c.4-1.5 1.1-2.8 1.9-4zM4.3 14a8.2 8.2 0 0 1 0-4h3.4a16 16 0 0 0 0 4zm.8 2h3a15.6 15.6 0 0 0 1.4 3.6A8 8 0 0 1 5.1 16zm3-8h-3a8 8 0 0 1 4.4-3.6A15.6 15.6 0 0 0 8.1 8zM12 20c-.8-1.2-1.5-2.5-1.9-4h3.8c-.4 1.5-1.1 2.8-1.9 4zm2.3-6H9.7a14.6 14.6 0 0 1 0-4h4.6a14.6 14.6 0 0 1 0 4zm.2 5.6a15.6 15.6 0 0 0 1.4-3.6h3a8 8 0 0 1-4.4 3.6zm1.8-5.6a16 16 0 0 0 0-4h3.4a8.2 8.2 0 0 1 0 4z"/></svg>
    </li>
    <li class="contact__item">P.O. Box 40218 Calloway, TX 79540
      <svg class="contact__icon" viewBox="0 0 24 24" aria-hidden="true"><path d="M12 2a7 7 0 0 0-7 7c0 5.2 7 13 7 13s7-7.8 7-13a7 7 0 0 0-7-7zm0 9.5A2.5 2.5 0 1 1 12 6.5a2.5 2.5 0 0 1 0 5z"/></svg>
    </li>
    <li class="contact__item contact__item--plain">275 Garnet Ln Delmora, Texas 79302</li>
  </ul>
</section>

<section class="card card--back" aria-label="Card back">
  <div class="brand-disc"></div>
  <span class="brand-name">DURMACK VINEX</span>
</section>

</body>
</html>
```